Willowmere Rites Studio creates individual, personalised ceremonies to celebrate weddings, naming days,coming of age, significant age, divorce and final resting rites. Ceremonies and meaningful rituals are created in collaboration with the individual to reflect their hopes and desires, how they will/have embrace/d their lives. The final design should have the logo (purple) on a white/silver background on the right hand side of the card. Name of business and contact details in red on a black background on the left
Updates

Hi All, have only just realised I have paid for a double sided card, yep, a newbie! Sorry to set the cat amongst the pigeons but could we put 'creating...... etc' on the back?

Target Market(s)

Couples marrying, renewing of vows, baby naming days, coming of age, significant age, divorce, funeral ceremonies. The target market predominantly will be couples marrying.

Industry/Entity Type

Business

Contact Information for Business Card

Willowmere Rites Studio, Tamsin Crowther, 0492-718305 willowmereritesstudio1@quillpost.net
"Crafting singular, bespoke occasions honouring journeys"

Font styles to use
Script

Colors
eb1f27
6b449b
f3f0f8

Requirements
Must have
• On initial entry, and now, the logo was not displayed in full - the bottom part was cut off - this needs to be in it's entirety. Colours as previously specified are non-negotiable. Font and placement of characters will be assessed as produced.
Should not have
• Telephone symbol, call us, director,grammatical symbols ( : )

```html
<!DOCTYPE html>
<html lang="en">
<head>
<meta charset="utf-8">
<title>Willowmere Rites Studio – Business Card Options</title>
<link rel="stylesheet" href="https://fonts.googleapis.com/css2?family=Marcellus+SC&family=Italianno&display=swap">
<style>
  :root {
    --stage-deep: #0d2a44;
    --stage-light: #1d5a80;
    --card-paper: #f3f0f8;
    --card-paper-edge: #e4e0ea;
    --shadow-grey: #a7a4ad;
    --violet: #6b449b;
    --violet-bright: #8a4fd6;
    --violet-text: #7a50c4;
    --red: #eb1f27;
    --red-dark: #b01a22;
    --white: #ffffff;
  }
  * { box-sizing: border-box; margin: 0; padding: 0; }
  html, body { width: 1200px; height: 841px; overflow: hidden; }
  body {
    background: radial-gradient(ellipse at 50% 45%, var(--stage-light) 0%, var(--stage-deep) 80%);
    position: relative;
  }
  .card {
    position: absolute;
    left: 308px;
    width: 621px;
    height: 382px;
    background: linear-gradient(160deg, var(--card-paper) 60%, var(--card-paper-edge));
    overflow: hidden;
  }
  .card--violet { top: 27px; --accent: var(--violet-text); }
  .card--red { top: 428px; --accent: var(--red); }
  .card__art { position: absolute; inset: 0; }
  .card__frame { stroke: var(--accent); fill: none; stroke-width: 1.5; }
  .card__rule { stroke: var(--accent); stroke-width: 1.3; }
  .card__rule-dot { fill: var(--accent); }

  .brand-mark {
    position: absolute;
    left: 10px;
    top: 165px;
    width: 90px;
    text-align: center;
    font-family: "Marcellus SC", serif;
    font-size: 13px;
    line-height: 1.3;
    color: var(--white);
  }
  .card__text {
    position: absolute;
    left: 110px;
    width: 466px;
    text-align: center;
    color: var(--accent);
    white-space: nowrap;
  }
  .business-name {
    font-family: "Marcellus SC", serif;
    font-size: 33px;
    line-height: 34px;
    height: 34px;
  }
  .business-name--first { top: 29px; }
  .business-name--second { top: 76px; }
  .contact-name { top: 150px; font-family: "Marcellus SC", serif; font-size: 24px; line-height: 28px; }
  .contact-phone { top: 188px; font-family: "Marcellus SC", serif; font-size: 28px; line-height: 32px; letter-spacing: 0.5px; }
  .contact-email { top: 228px; font-family: "Italianno", cursive; font-size: 26px; line-height: 28px; }
  .tagline { top: 313px; left: 90px; width: 500px; font-family: "Italianno", cursive; font-size: 27px; line-height: 30px; }
</style>
</head>
<body>

<section class="card card--violet">
  <svg class="card__art" width="621" height="382" viewBox="0 0 621 382">
    <defs>
      <linearGradient id="band-violet" x1="0" y1="0" x2="1" y2="0.4">
        <stop offset="0" stop-color="var(--violet)"/>
        <stop offset="1" stop-color="var(--violet-bright)"/>
      </linearGradient>
    </defs>
    <rect class="card__frame" x="60" y="16" width="536" height="344"/>
    <path d="M0 0 H12 C190 95 190 287 12 382 H0 Z" fill="var(--shadow-grey)"/>
    <path d="M0 0 C170 95 170 287 0 382 Z" fill="url(#band-violet)"/>
    <line class="card__rule" x1="228" y1="70" x2="456" y2="70"/>
    <circle class="card__rule-dot" cx="342" cy="70" r="2.5"/>
    <line class="card__rule" x1="235" y1="267" x2="449" y2="267"/>
    <circle class="card__rule-dot" cx="342" cy="267" r="2.2"/>
  </svg>
  <div class="brand-mark">Willowmere<br>Rites<br>Studio</div>
  <p class="card__text business-name business-name--first">Willowmere Rites</p>
  <p class="card__text business-name business-name--second">Studio</p>
  <p class="card__text contact-name">Tamsin Crowther</p>
  <p class="card__text contact-phone">0492-718305</p>
  <p class="card__text contact-email">willowmereritesstudio1@quillpost.net</p>
  <p class="card__text tagline">Crafting singular, bespoke occasions honouring journeys</p>
</section>

<section class="card card--red">
  <svg class="card__art" width="621" height="382" viewBox="0 0 621 382">
    <defs>
      <linearGradient id="band-red" x1="0" y1="0" x2="1" y2="0.4">
        <stop offset="0" stop-color="var(--red)"/>
        <stop offset="1" stop-color="var(--red-dark)"/>
      </linearGradient>
    </defs>
    <rect class="card__frame" x="60" y="16" width="536" height="344"/>
    <path d="M0 0 H12 C190 95 190 287 12 382 H0 Z" fill="var(--shadow-grey)"/>
    <path d="M0 0 C170 95 170 287 0 382 Z" fill="url(#band-red)"/>
    <line class="card__rule" x1="228" y1="70" x2="456" y2="70"/>
    <circle class="card__rule-dot" cx="342" cy="70" r="2.5"/>
    <line class="card__rule" x1="235" y1="267" x2="449" y2="267"/>
    <circle class="card__rule-dot" cx="342" cy="267" r="2.2"/>
  </svg>
  <div class="brand-mark">Willowmere<br>Rites<br>Studio</div>
  <p class="card__text business-name business-name--first">Willowmere Rites</p>
  <p class="card__text business-name business-name--second">Studio</p>
  <p class="card__text contact-name">Tamsin Crowther</p>
  <p class="card__text contact-phone">0492-718305</p>
  <p class="card__text contact-email">willowmereritesstudio1@quillpost.net</p>
  <p class="card__text tagline">Crafting singular, bespoke occasions honouring journeys</p>
</section>

</body>
</html>
```